International Bottled Water Company Needs a Unique Bottle Design

We are expanding our product range to include a new bottled water range. We will be using our own bottle moulds, hence we require innovative and attractive designs for the bottle design. We want it to look classy and yet easy to hold. Volumes that we are looking at are 300ml, 500ml and 1.5L (PET, glass is optional). We will be aiming to have this brand as a premium brand such as Pellik, Drim, Kolindu etc. Please use them as examples. Definitely will welcome other innovative designs.
Updates

Dear all,

Just to give you an idea of the type of design I would like is Kolindu Water from NZ. The way they designed the PET bottle was great, it looked like Glass even though it was PET. Perhaps we can work on that?

Thanks!

Pol

Dear all,

I have a few updates on the brand:

1. It is from a French Source
2. The brand is named after a lake - so lake and mountain motives on the bottle are desirable

I will be also posting some pics of the bottles I like on the brief, so please go to the brief and have a look at them.

Thanks very much. 

Pol 

Target Market(s)

Our target market will be the middle to upper segment of the consumer.

Industry/Entity Type

It Company

Requirements
Must have
• 300ml, 500ml and 1.5L designs. The bottle shape must be feasible for production (ie be able to be translated from graphics to real life).
Nice to have
• Classy, elegant bottle

```html
<!DOCTYPE html>
<html lang="en">
<head>
<meta charset="utf-8">
<title>Veloran Springs – 500 mL Bottle</title>
<link rel="stylesheet" href="https://fonts.googleapis.com/css2?family=Roboto:wght@300;400&display=swap">
<style>
  :root {
    --page-bg: #ffffff;
    --bottle-fill: #eef1f4;
    --bottle-edge: #d3d9df;
    --cap-fill: #f3f4f5;
    --cap-edge: #c9ced3;
    --label-fill: #fbfcfd;
    --brand-blue: #29aee3;
    --brand-blue-deep: #1e92cc;
    --caption: #6b5d8c;
  }
  html, body {
    margin: 0;
    padding: 0;
    width: 1200px;
    height: 2372px;
    overflow: hidden;
    background: var(--page-bg);
  }
  .canvas {
    position: relative;
    width: 1200px;
    height: 2372px;
    font-family: "Roboto", Arial, sans-serif;
  }
  .bottle-art {
    position: absolute;
    inset: 0;
  }
  .brand-name,
  .brand-sub {
    position: absolute;
    margin: 0;
    line-height: 1;
    font-weight: 300;
    white-space: nowrap;
    transform: rotate(-90deg);
    transform-origin: 0 0;
  }
  .brand-name {
    left: 508px;
    top: 1372px;
    font-size: 92px;
    color: var(--brand-blue);
    letter-spacing: 1px;
  }
  .brand-sub {
    left: 598px;
    top: 1376px;
    font-size: 58px;
    color: var(--brand-blue-deep);
  }
  .product-type,
  .product-volume {
    position: absolute;
    left: 0;
    width: 1200px;
    margin: 0;
    text-align: center;
    color: var(--caption);
    font-weight: 400;
  }
  .product-type {
    top: 1786px;
    font-size: 20px;
    letter-spacing: 0.5px;
  }
  .product-volume {
    top: 1828px;
    font-size: 18px;
  }
</style>
</head>
<body>
<div class="canvas">
  <svg class="bottle-art" width="1200" height="2372" viewBox="0 0 1200 2372" aria-hidden="true">
    <!-- cap -->
    <rect class="cap" x="527" y="4" width="161" height="132" rx="14" fill="var(--cap-fill)" stroke="var(--cap-edge)" stroke-width="3"/>
    <rect class="neck-ring" x="512" y="140" width="191" height="26" rx="10" fill="var(--cap-fill)" stroke="var(--cap-edge)" stroke-width="3"/>
    <!-- bottle body -->
    <path class="bottle-body"
      d="M540 166
         L676 166
         C690 250 760 310 860 360
         C920 390 944 430 944 480
         L944 1000
         C944 1040 905 1060 905 1120
         C905 1190 944 1220 944 1300
         L944 2290
         C944 2340 915 2366 860 2366
         L374 2366
         C319 2366 290 2340 290 2290
         L290 1300
         C290 1220 329 1190 329 1120
         C329 1060 290 1040 290 1000
         L290 480
         C290 430 314 390 374 360
         C474 310 526 250 540 166 Z"
      fill="var(--bottle-fill)" stroke="var(--bottle-edge)" stroke-width="4"/>
    <!-- label -->
    <path class="label"
      d="M290 486 L944 486 L944 1000
         C944 1040 905 1060 905 1120
         C905 1190 944 1220 944 1300
         L944 2194 L290 2194 L290 1300
         C290 1220 329 1190 329 1120
         C329 1060 290 1040 290 1000 Z"
      fill="var(--label-fill)"/>
    <rect class="label-band label-band--top" x="290" y="486" width="654" height="131" fill="var(--brand-blue)"/>
    <rect class="label-band label-band--bottom" x="290" y="2064" width="654" height="130" fill="var(--brand-blue)"/>
    <!-- brand mark -->
    <circle class="brand-dot" cx="596" cy="1520" r="120" fill="var(--brand-blue)"/>
  </svg>

  <p class="brand-name">Veloran</p>
  <p class="brand-sub">Springs</p>
  <p class="product-type">NATURAL MINERAL WATER</p>
  <p class="product-volume">500 mL</p>
</div>
</body>
</html>
```